Etiketten-Design für Weinflasche
Helga hat mit sehr viel Mühe und Hingabe unsere Wünsche umgesetzt. Wir sind mit dem Endergebnis sehr zufrieden.
Zielgruppe
Wir sind ein Weingut-Startup und suchen ein frisches, hochwertiges Design für unsere Flaschenetiketten.
Aufgabenstellung
Wir benötigen ein Vorderetikett für unsere Weinflaschen mit folgenden Vorgaben:
- Etiketten sollen variabel nutzbar sein, für verschiedene Rebsorten bspw. in versch. Farben
- Auf dem Etikett zwingend: Logo (siehe Anlage), Rebsorte, Anbaugebiet (Nahe)
- Wiedererkennungswert
- nicht zu klassisch, nicht zu futuristisch (gutes Mittelmaß, wie beim Logo auch)
- ggf. Spiel mit (Hintergrund-)Farben für verschiedene Sorten, ggf. Hintergrundmuster (evtl. Höhenlinien des Talwiesers, Bad Kreuznach (unser Heimatberg))
- Anpassung an verschiedene Qualitätsstufen (Gutswein, Ortswein, Lagenwein), ggf. schwarzes Sonderetikett für absolutes Premiumsegment
- unsere Werte als Naturnah und familiengeführtes Weingut sollen transportiert werden
- Maß: 80x90mm (breitxhoch)
Insgesamt sind wir offen für verschiedene Vorschläge, auch wenn die Vorgaben oben teils sehr konkret sind. Bei guten Designs lassen wir uns gerne von unseren Vorstellungen abbringen ;)

```html
<!DOCTYPE html>
<html lang="de">
<head>
<meta charset="utf-8">
<title>Lindhoff Weingut – Dornfelder Feinherb Etikett</title>
<link rel="stylesheet" href="https://fonts.googleapis.com/css2?family=Playfair+Display:wght@600&family=Montserrat:wght@400;500&display=swap">
<style>
  :root {
    --page: #ffffff;
    --black: #080808;
    --metal-dark: #1e1e1e;
    --metal-low: #2e2e2e;
    --metal-mid: #4a4a4a;
    --metal-soft: #7a7a7a;
    --metal-light: #a8a8a8;
    --metal-edge: #5e5e5e;
    --logo-green: #8c9b3e;
    --title-white: #f4f4f4;
    --quality-grey: #d2d2d2;
    --region-grey: #8a8a8a;
    --rule-grey: #2a2a2a;
    --vine-grey: #7d7d7d;
  }
  * { margin: 0; padding: 0; box-sizing: border-box; }
  html, body {
    width: 1200px; height: 1199px; overflow: hidden;
    background: var(--page);
  }
  .label {
    position: absolute; left: 220px; top: 90px;
    width: 760px; height: 1020px; overflow: hidden;
    background: linear-gradient(90deg, var(--metal-dark) 0%, var(--metal-low) 30%, var(--metal-mid) 60%, var(--metal-soft) 80%, var(--metal-light) 92%, var(--metal-edge) 100%);
    font-family: "Montserrat", sans-serif;
  }
  .panel {
    position: absolute; left: 0; right: 0;
    background: var(--black);
  }
  .panel--head { top: 0; height: 300px; right: 66px; }
  .panel--body {
    top: 330px; height: 460px;
    background: linear-gradient(180deg, #101010 0%, var(--black) 60%, #141414 100%);
  }
  .brand {
    position: absolute; top: 92px; left: 0; width: 694px;
    text-align: center; color: var(--logo-green);
  }
  .brand__name {
    font-family: "Playfair Display", serif; font-weight: 600;
    font-size: 84px; line-height: 1;
  }
  .brand__sub {
    font-size: 18px; letter-spacing: 6px; margin-top: 6px;
  }
  .wine-title {
    position: absolute; left: 166px; top: 466px;
    font-family: "Playfair Display", serif; font-weight: 600;
    font-size: 60px; line-height: 1.15; color: var(--title-white);
    letter-spacing: 1px;
  }
  .vine-art {
    position: absolute; left: 630px; top: 400px; width: 130px; height: 350px;
    border-radius: 60px 0 0 60px;
    background: radial-gradient(ellipse at 60% 45%, var(--vine-grey) 0%, #5a5a5a 50%, #2a2a2a 100%);
  }
  .region {
    position: absolute; left: 445px; top: 716px;
    font-size: 26px; font-weight: 500; letter-spacing: 9px; color: var(--region-grey);
  }
  .quality {
    position: absolute; right: 258px; top: 838px;
    text-align: right; font-size: 19px; line-height: 1.5; color: var(--quality-grey);
    letter-spacing: 0.5px;
  }
  .divider {
    position: absolute; left: 516px; top: 822px; width: 2px; height: 198px;
    background: var(--rule-grey);
  }
  .vintage {
    position: absolute; left: 534px; top: 842px;
    font-size: 46px; font-weight: 400; color: var(--title-white);
  }
</style>
</head>
<body>
  <main class="label">
    <div class="panel panel--head"></div>
    <div class="panel panel--body"></div>

    <div class="brand">
      <div class="brand__name">Lindhoff</div>
      <div class="brand__sub">WEINGUT</div>
    </div>

    <h1 class="wine-title">DORNFELDER<br>FEINHERB</h1>

    <div class="vine-art" role="img" aria-label="Weinranke mit Blättern und Traube in Grau"></div>

    <div class="region">NAHE</div>

    <div class="quality">DEUTSCHER<br>QUALITÄTSWEIN</div>
    <div class="divider"></div>
    <div class="vintage">2024</div>
  </main>
</body>
</html>
```